Advertising company unique advertising platform

we need a logo design for a new company based in Australia Melbourne. We develop innovated advertising platform where consumer can use this platform to get regular discount, as business owner they can use this platform for free advertisement. Payment for this advertisement platform only payable every two weeks, when I generate revenue for their business

Industry/Entity Type

Advertising

Contact Information for Business Card

Dale Pruitt | Co-Founder |Managing Director
Suite 718 263 Harrowgate Row Melbourne Vic 3000

ABN 41 902 615 273
Tel: +61 0491 528 307 | Email: dale.pruitt@corvelaxtro.com

Font styles to use
Decorative
Script

Requirements
Must have
• Try few different design and some round corner business card
Should not have
• One round corner business card...try 4 different colour background not only black, make sure two side is designed. Be creative so imagine you are giving this to a client make sure has wow factor, if you can also try one design with engrave like all the logo, words look 3d feel
• The word Advertising Platform use attached file font

```html
<!DOCTYPE html>
<html lang="en">
<head>
<meta charset="utf-8">
<title>Brightlane — Business Card</title>
<link rel="stylesheet" href="https://fonts.googleapis.com/css2?family=Montserrat:wght@400;500;600&display=swap">
<style>
  :root {
    --page: #e9e6e1;
    --card-dark: #262626;
    --accent-red: #e8432b;
    --brand-orange: #f0812f;
    --grad-green: #62c59b;
    --grad-blue: #86a7dc;
    --grad-sky: #5fb5e2;
    --ink: #1e2230;
    --white: #ffffff;
  }
  * { box-sizing: border-box; margin: 0; padding: 0; }
  html, body { width: 1200px; height: 1200px; overflow: hidden; }
  body {
    background: var(--page);
    font-family: "Montserrat", Arial, sans-serif;
    position: relative;
  }
  .card {
    position: absolute;
    left: 180px;
    width: 840px;
    height: 480px;
    border-radius: 6px;
    overflow: hidden;
    box-shadow: 0 14px 30px rgba(0,0,0,0.22);
  }
  .card--front { top: 90px; background: var(--card-dark); display: flex; align-items: center; justify-content: center; }
  .card--back { top: 630px; display: flex; }

  .brand { display: flex; align-items: center; gap: 18px; }
  .brand__dot { width: 34px; height: 34px; border-radius: 50%; background: var(--brand-orange); }
  .brand__name { color: var(--brand-orange); font-weight: 600; font-size: 60px; letter-spacing: 1px; }

  .back__identity {
    width: 360px; background: var(--card-dark);
    display: flex; flex-direction: column; align-items: center; justify-content: center; gap: 18px;
  }
  .back__identity .brand__name { font-size: 44px; }
  .back__identity .brand__dot { width: 26px; height: 26px; }
  .abn { color: var(--white); font-size: 17px; letter-spacing: 0.5px; }

  .back__stripe { width: 10px; background: var(--accent-red); }

  .back__details {
    flex: 1;
    background: linear-gradient(135deg, var(--grad-green) 0%, var(--grad-blue) 70%, var(--grad-sky) 100%);
    color: var(--ink);
    padding: 60px 40px 0 58px;
  }
  .row { display: flex; gap: 16px; align-items: flex-start; }
  .row svg { flex: none; width: 20px; height: 20px; fill: var(--ink); margin-top: 3px; }
  .person__name { font-size: 38px; font-weight: 600; line-height: 1; }
  .person__role { font-size: 17px; line-height: 1.35; margin: 10px 0 0 36px; }
  .address { margin-top: 38px; font-size: 17px; line-height: 1.4; }
  .contacts { margin-top: 42px; display: flex; flex-direction: column; gap: 10px; font-size: 17px; }
</style>
</head>
<body>
  <section class="card card--front">
    <div class="brand">
      <span class="brand__dot"></span>
      <span class="brand__name">Brightlane</span>
    </div>
  </section>

  <section class="card card--back">
    <div class="back__identity">
      <div class="brand">
        <span class="brand__dot"></span>
        <span class="brand__name">Brightlane</span>
      </div>
      <p class="abn">ABN : 41 902 615 273</p>
    </div>
    <div class="back__stripe"></div>
    <div class="back__details">
      <div class="row">
        <svg viewBox="0 0 20 20"><circle cx="10" cy="6" r="4.5"/><path d="M1 20c0-5 4-8 9-8s9 3 9 8z"/></svg>
        <h1 class="person__name">Dale Pruitt</h1>
      </div>
      <p class="person__role">Co-Founder<br>Managing Director</p>

      <div class="row address">
        <svg viewBox="0 0 20 20"><path d="M10 0a7 7 0 0 0-7 7c0 5 7 13 7 13s7-8 7-13a7 7 0 0 0-7-7zm0 10a3 3 0 1 1 0-6 3 3 0 0 1 0 6z"/></svg>
        <p>Suite 718 263<br>Harrowgate Row<br>Melbourne Vic 3000</p>
      </div>

      <div class="contacts">
        <div class="row">
          <svg viewBox="0 0 20 20"><path d="M4 1l4 4-2 3c1 3 3 5 6 6l3-2 4 4-3 3C8 19 1 12 1 4z"/></svg>
          <span>+61 0491 528 307</span>
        </div>
        <div class="row">
          <svg viewBox="0 0 20 20"><path d="M1 4h18v12H1z M1 4l9 7 9-7" fill="none" stroke="#1e2230" stroke-width="2"/></svg>
          <span>dale.pruitt@corvelaxtro.com</span>
        </div>
      </div>
    </div>
  </section>
</body>
</html>
```